Marlowe Shopcraft Interiors web design

We need to relaunch my commercial and retail interior design + construction company after being out of the industry's for 10 plus years.

```html
<!DOCTYPE html>
<html lang="en">
<head>
<meta charset="utf-8">
<title>Marlowe Shopcraft Interiors</title>
<link href="https://fonts.googleapis.com/css2?family=Krona+One&family=Montserrat:wght@400;500;600;700&display=swap" rel="stylesheet">
<style>
:root{
  --blue:#0a8df5;
  --ink:#111318;
  --dark:#1c1d20;
  --muted:#555a61;
  --line:#d9dde2;
  --grey:#f0f0f0;
  --white:#ffffff;
  --display:"Krona One", sans-serif;
  --body:"Montserrat", sans-serif;
}
*{box-sizing:border-box;margin:0;padding:0}
html,body{width:1200px;height:2658px;overflow:hidden;background:var(--white);font-family:var(--body);color:var(--ink)}
.page{position:relative;width:1200px;height:2658px}
.abs{position:absolute}
.display{font-family:var(--display);text-transform:uppercase;letter-spacing:1.5px;font-weight:400}

/* header + hero */
.hero{left:0;top:0;width:1200px;height:617px;background:linear-gradient(180deg,#1d2533 0%,#2a3140 35%,#3a3125 70%,#241c14 100%)}
.brand{display:flex;align-items:center;gap:8px;color:var(--white)}
.brand-mark{width:14px;height:14px;background:var(--blue)}
.brand-name{font-family:var(--body);font-weight:700;font-size:13px;line-height:14px;text-transform:uppercase;width:120px}
.nav{top:26px;left:523px;display:flex;gap:30px;font-size:10px;font-weight:500;color:var(--white);letter-spacing:.3px}
.search{left:899px;top:24px}
.socials{left:980px;top:22px;display:flex;gap:7px}
.socials span{width:21px;height:21px;background:var(--blue)}
.hero-title{left:111px;top:218px;font-size:29px;line-height:38px;color:var(--white);letter-spacing:2px;white-space:nowrap}
.hero-title em{font-style:normal;color:var(--blue)}
.hero-sub{left:112px;top:297px;width:410px;font-size:15px;line-height:20px;color:var(--white)}
.btn{display:inline-flex;align-items:center;justify-content:center;background:var(--blue);color:var(--white);font-weight:600;font-size:12px;letter-spacing:.5px;text-transform:uppercase}
.hero-btn{left:112px;top:356px;width:125px;height:39px}
.slider-tabs{left:112px;top:577px;width:216px;height:40px;background:var(--blue);display:flex;align-items:center;gap:33px;padding-left:31px;font-size:11px;font-weight:700;color:#8ec8fb}
.slider-tabs .on{color:var(--white)}

/* services */
.section-title{font-size:21px;letter-spacing:2px;text-align:center;width:1200px;left:0}
.card{width:317px;border:1px solid var(--line);background:var(--white)}
.card.active{background:var(--blue);border-color:var(--blue);color:var(--white)}
.card h3{position:absolute;left:90px;font-size:14px;font-weight:600;line-height:18px}
.card p{position:absolute;left:19px;width:250px;font-size:10px;line-height:14px;color:var(--muted)}
.card.active p{color:var(--white)}
.card .icon{position:absolute;left:22px;top:12px}
.card .go{position:absolute;right:0;bottom:0;width:42px;height:27px;background:var(--blue);display:flex;align-items:center;justify-content:center}
.card.active .go{background:var(--white)}

/* approach */
.approach-title{left:112px;top:1170px;width:530px;font-size:21px;line-height:28px;letter-spacing:1.5px;white-space:nowrap}
.approach-text{left:112px;top:1322px;width:500px;font-size:10.5px;line-height:15.5px;color:var(--muted)}
.approach-btn{left:112px;top:1405px;width:114px;height:35px;font-size:11px}
.approach-img{left:660px;top:1125px;width:540px;height:328px;background:linear-gradient(135deg,#e7eaee,#c9ced5 60%,#f3f4f6)}

/* why choose */
.why{left:0;top:1515px;width:1200px;height:405px;background:var(--grey)}
.why-title{left:112px;top:1572px;font-size:21px;line-height:28px;letter-spacing:1.5px}
.arrow-btn{width:38px;height:38px;display:flex;align-items:center;justify-content:center}
.arrow-btn.outline{border:1px solid var(--blue);background:var(--white)}
.arrow-btn.solid{background:var(--blue)}
.why-card{top:1652px;height:206px;background:linear-gradient(160deg,#4a4f57,#2b2e33)}
.why-card.alt{background:linear-gradient(160deg,#c9b8a8,#7a6b60)}
.why-caption{position:absolute;left:0;bottom:0;width:372px;height:113px;background:rgba(30,32,36,.85);padding:14px 25px;color:var(--white)}
.why-caption.blue{background:rgba(10,141,245,.92)}
.why-caption h4{font-family:var(--display);text-transform:uppercase;font-size:12.5px;letter-spacing:1.5px;margin-bottom:8px;font-weight:400}
.why-caption p{font-size:10.5px;line-height:15.5px}

/* teams */
.team{top:2024px;height:236px}
.team-photo{position:absolute;inset:0}
.team-cap{position:absolute;left:0;bottom:0;color:var(--white)}
.team-cap h4{font-family:var(--display);text-transform:uppercase;font-weight:400;font-size:11px;line-height:16px;letter-spacing:1.5px}
.team-cap .more{font-size:10px;font-weight:600;color:var(--blue);text-decoration:underline;margin-top:8px;display:block}

/* newsletter */
.news{left:0;top:2323px;width:1200px;height:201px;background:linear-gradient(180deg,var(--blue),#0c7fe0)}
.news-title{left:0;width:1200px;top:2380px;text-align:center;color:var(--white);font-size:21px;letter-spacing:2px}
.news-sub{left:0;width:1200px;top:2409px;text-align:center;color:var(--white);font-size:10.5px}
.news-input{left:413px;top:2432px;width:240px;height:32px;border:1px solid var(--white);color:var(--white);font-size:10.5px;padding:10px 17px}
.news-btn{left:660px;top:2432px;width:127px;height:32px;background:var(--white);color:var(--blue);font-size:11px}

/* footer */
.footer{left:0;top:2524px;width:1200px;height:134px;background:var(--dark)}
.foot-nav{left:437px;top:2579px;display:flex;gap:31px;color:var(--white);font-size:10px;font-weight:500}
.copy{left:0;width:1200px;top:2605px;text-align:center;color:var(--white);font-size:10px}
.follow{left:912px;top:2578px;display:flex;align-items:center;gap:14px;color:var(--white);font-size:11px;font-weight:700}
.follow i{width:12px;height:12px;border-radius:50%;background:var(--blue);display:block}
</style>
</head>
<body>
<div class="page">

  <!-- hero -->
  <section class="abs hero" role="img" aria-label="Night city skyline with a tall illuminated skyscraper"></section>
  <div class="abs brand" style="left:112px;top:29px">
    <span class="brand-mark"></span>
    <span class="brand-name">Marlowe Shopcraft Interiors</span>
  </div>
  <nav class="abs nav"><span>WHY CHOOSE US</span><span>OUR EXPERT TEAMS</span><span>OUR SERVICES</span></nav>
  <svg class="abs search" width="16" height="16" viewBox="0 0 16 16"><circle cx="6.5" cy="6.5" r="5" fill="none" stroke="#fff" stroke-width="1.3"/><line x1="10.3" y1="10.3" x2="14.5" y2="14.5" stroke="#fff" stroke-width="1.3"/></svg>
  <div class="abs socials"><span></span><span></span><span></span><span></span></div>

  <h1 class="abs display hero-title">Welcome to Marlowe<br><em>Shopcraft</em> Interiors</h1>
  <p class="abs hero-sub">Have you experienced frustration in the building and design process?</p>
  <a class="abs btn hero-btn">Learn more</a>
  <div class="abs slider-tabs"><span class="on">01</span><span>02</span><span>03</span><span style="color:#fff">&lsaquo; &rsaquo;</span></div>

  <!-- services -->
  <h2 class="abs display section-title" style="top:674px">Services we offer</h2>

  <div class="abs card" style="left:111px;top:719px;height:127px">
    <svg class="icon" width="50" height="50" viewBox="0 0 50 50" fill="none" stroke="#333" stroke-width="1.3"><circle cx="20" cy="20" r="15"/><ellipse cx="20" cy="20" rx="8" ry="5"/><circle cx="20" cy="20" r="2"/><line x1="31" y1="31" x2="45" y2="45" stroke-width="3"/></svg>
    <h3 style="top:22px">Site Inspection</h3>
    <p style="top:66px">Pre-lease site inspections and advice on base building works.</p>
    <span class="go"><svg width="16" height="8"><path d="M0 4h14M11 1l3 3-3 3" stroke="#fff" fill="none"/></svg></span>
  </div>
  <div class="abs card active" style="left:441px;top:719px;height:127px">
    <svg class="icon" width="50" height="50" viewBox="0 0 50 50" fill="none" stroke="#fff" stroke-width="1.4"><path d="M17 12h16l-4 6c8 4 12 12 10 20-2 6-28 6-30 0-2-8 2-16 10-20z"/><text x="19" y="38" fill="#fff" stroke="none" font-size="16">$</text></svg>
    <h3 style="top:22px">Budgeting</h3>
    <p style="top:66px">Expert advice on construction budgets and required services.</p>
    <span class="go"><svg width="16" height="8"><path d="M0 4h14M11 1l3 3-3 3" stroke="#0a8df5" fill="none"/></svg></span>
  </div>
  <div class="abs card" style="left:770px;top:719px;height:127px">
    <svg class="icon" width="50" height="50" viewBox="0 0 50 50" fill="none" stroke="#333" stroke-width="1.3"><circle cx="24" cy="24" r="21"/><path d="M12 26l12-11 12 11M16 23v12h16V23M21 35v-7h6v7"/></svg>
    <h3 style="top:22px">Renovations and<br>Rebranding</h3>
    <p style="top:66px">Vacant and demolishing works, shop front renovations, signage updates, and removals.</p>
    <span class="go"><svg width="16" height="8"><path d="M0 4h14M11 1l3 3-3 3" stroke="#fff" fill="none"/></svg></span>
  </div>

  <div class="abs card" style="left:111px;top:859px;height:120px">
    <svg class="icon" width="50" height="50" viewBox="0 0 50 50" fill="none" stroke="#333" stroke-width="1.3"><path d="M24 4a21 21 0 1 0 21 21H24z"/><path d="M28 2v19h19A19 19 0 0 0 28 2z"/><text x="12" y="32" fill="#333" stroke="none" font-size="14">$</text></svg>
    <h3 style="top:22px">Planning Services</h3>
    <p style="top:66px">Comprehensive planning from start to finish.</p>
    <span class="go"><svg width="16" height="8"><path d="M0 4h14M11 1l3 3-3 3" stroke="#fff" fill="none"/></svg></span>
  </div>
  <div class="abs card" style="left:441px;top:859px;height:120px">
    <svg class="icon" width="50" height="50" viewBox="0 0 50 50" fill="none" stroke="#333" stroke-width="1.3"><rect x="3" y="6" width="40" height="32"/><line x1="3" y1="13" x2="43" y2="13"/><path d="M15 21l-5 5 5 5M31 21l5 5-5 5M26 19l-6 14"/></svg>
    <h3 style="top:22px">Permit Applications</h3>
    <p style="top:66px">Assistance in obtaining building, health, and town planning permits.</p>
    <span class="go"><svg width="16" height="8"><path d="M0 4h14M11 1l3 3-3 3" stroke="#fff" fill="none"/></svg></span>
  </div>
  <div class="abs card" style="left:770px;top:859px;height:120px">
    <svg class="icon" width="50" height="50" viewBox="0 0 50 50" fill="none" stroke="#333" stroke-width="1.3"><circle cx="22" cy="22" r="19"/><path d="M13 22l6 6 12-13"/></svg>
    <h3 style="top:22px">Design Approval</h3>
    <p style="top:66px">Submission and approval processes for design fitouts in shopping centers.</p>
    <span class="go"><svg width="16" height="8"><path d="M0 4h14M11 1l3 3-3 3" stroke="#fff" fill="none"/></svg></span>
  </div>

  <div class="abs card" style="left:111px;top:992px;height:120px">
    <svg class="icon" width="50" height="50" viewBox="0 0 50 50" fill="none" stroke="#333" stroke-width="1.3"><path d="M24 4a21 21 0 1 0 21 21H24z"/><path d="M28 2v19h19A19 19 0 0 0 28 2z"/><text x="12" y="32" fill="#333" stroke="none" font-size="14">$</text></svg>
    <h3 style="top:22px">Consultation</h3>
    <p style="top:66px">Collaborate with disability access consultants, architects, interior designers, and various engineering disciplines.</p>
    <span class="go"><svg width="16" height="8"><path d="M0 4h14M11 1l3 3-3 3" stroke="#fff" fill="none"/></svg></span>
  </div>
  <div class="abs card" style="left:441px;top:992px;height:120px">
    <svg class="icon" width="50" height="50" viewBox="0 0 50 50" fill="none" stroke="#333" stroke-width="1.3"><circle cx="15" cy="30" r="12"/><path d="M22 14a13 11 0 1 1 8 19l-4 4v-5"/><text x="11" y="35" fill="#333" stroke="none" font-size="12">?</text><path d="M28 14h12M28 19h12M28 24h8"/></svg>
    <h3 style="top:22px">Design and Construction</h3>
    <p style="top:66px">Seamless coordination of design and construction solutions.</p>
    <span class="go"><svg width="16" height="8"><path d="M0 4h14M11 1l3 3-3 3" stroke="#fff" fill="none"/></svg></span>
  </div>
  <div class="abs card" style="left:770px;top:992px;height:120px">
    <svg class="icon" width="50" height="50" viewBox="0 0 50 50" fill="none" stroke="#333" stroke-width="1.3"><circle cx="22" cy="22" r="19"/><circle cx="22" cy="22" r="13"/><rect x="15" y="18" width="14" height="8" rx="4" transform="rotate(-45 22 22)"/></svg>
    <h3 style="top:22px">Dispensary Joinery</h3>
    <p style="top:66px">Specialized joinery solutions for dispensaries.</p>
    <span class="go"><svg width="16" height="8"><path d="M0 4h14M11 1l3 3-3 3" stroke="#fff" fill="none"/></svg></span>
  </div>

  <!-- approach -->
  <h2 class="abs display approach-title">Are you in search of a fresh<br>approach to guarantee<br>superior outcomes for your<br>upcoming commercial<br>and retail interior fitouts</h2>
  <p class="abs approach-text">At Marlowe Shopcraft Interiors, we were founded with your needs at the forefront—a dedication to delivering a transformative leap in results for your commercial and retail projects. Our pride lies in surpassing client expectations, achieved through meticulous planning and proactive problem-solving before challenges even surface.</p>
  <a class="abs btn approach-btn">Learn more</a>
  <div class="abs approach-img" role="img" aria-label="Pencil sketch of a modern glass commercial building"></div>

  <!-- why choose -->
  <section class="abs why"></section>
  <h2 class="abs display why-title">Why choose Marlowe<br>Shopcraft Interiors</h2>
  <span class="abs arrow-btn outline" style="left:999px;top:1578px"><svg width="8" height="12"><path d="M7 1L2 6l5 5" stroke="#0a8df5" fill="none" stroke-width="1.4"/></svg></span>
  <span class="abs arrow-btn solid" style="left:1050px;top:1578px"><svg width="8" height="12"><path d="M1 1l5 5-5 5" stroke="#fff" fill="none" stroke-width="1.4"/></svg></span>

  <div class="abs why-card" style="left:112px;width:398px" role="img" aria-label="Team members reviewing documents around a desk">
    <div class="why-caption"><h4>Holistic approach</h4><p>From concept to completion, we deliver client-focused results, providing a holistic, compliant, and innovative business approach.</p></div>
  </div>
  <div class="abs why-card alt" style="left:528px;width:398px" role="img" aria-label="Colleagues discussing work at a laptop">
    <div class="why-caption blue"><h4>Specialisations</h4><p>We specialise in a range of projects, including Medicinal Cannabis dispensaries, Medical centers, Pharmacy and health food outlets, Strongroom safe supply and installation, Offices, retail, hospitality, and showrooms.</p></div>
  </div>
  <div class="abs why-card" style="left:938px;width:262px;overflow:hidden" role="img" aria-label="Hands working on a tablet with charts">
    <div class="why-caption" style="width:262px;white-space:nowrap"><h4>Holistic approach</h4><p>From concept to completion, we deliver client-<br>results, providing a holistic, compliant, and in<br>business approach.</p></div>
  </div>

  <!-- teams -->
  <h2 class="abs display section-title" style="top:1976px">Our expert teams</h2>
  <div class="abs team" style="left:112px;width:478px">
    <div class="team-photo" role="img" aria-label="Building under construction with scaffolding" style="background:linear-gradient(180deg,#9a8e86,#6c6660)"></div>
    <div class="team-cap" style="width:441px;height:135px;background:rgba(10,141,245,.92);padding:22px 18px">
      <h4>Consulting team</h4>
      <p style="font-size:10.5px;line-height:15.5px;margin-top:6px">Our consulting team comprises project managers, interior designers, architects, town planners, acoustic, structural, mechanical, fire services engineers, building surveyors, and DDA consultants, ensuring compliant and innovative design and construction solutions.</p>
    </div>
  </div>
  <div class="abs team" style="left:613px;width:226px">
    <div class="team-photo" role="img" aria-label="Construction workers in hard hats reviewing plans on site" style="background:linear-gradient(180deg,#7d7f84,#b98a3c)"></div>
    <div class="team-cap" style="width:226px;height:96px;background:rgba(30,32,36,.85);padding:22px 19px"><h4>Construction<br>team</h4><span class="more">READ MORE</span></div>
  </div>
  <div class="abs team" style="left:862px;width:226px">
    <div class="team-photo" role="img" aria-label="Hand holding a key beside a small model house" style="background:linear-gradient(180deg,#8fb59a,#d9c5b4)"></div>
    <div class="team-cap" style="width:226px;height:96px;background:rgba(30,32,36,.85);padding:22px 19px"><h4>Finance and leagal<br>consulting</h4><span class="more">READ MORE</span></div>
  </div>

  <!-- newsletter -->
  <section class="abs news"></section>
  <h2 class="abs display news-title">Newsletter</h2>
  <p class="abs news-sub">Keep up our latest news and events. Subscribe our newsletter</p>
  <div class="abs news-input">Enter Your Email</div>
  <a class="abs btn news-btn">Subscribe</a>

  <!-- footer -->
  <footer class="abs footer"></footer>
  <div class="abs brand" style="left:112px;top:2580px">
    <span class="brand-mark"></span>
    <span class="brand-name">Marlowe Shopcraft Interiors</span>
  </div>
  <nav class="abs foot-nav"><span>WHY CHOOSE US</span><span>OUR EXPERT TEAMS</span><span>OUR SERVICES</span></nav>
  <p class="abs copy">COPYRIGHT © 2023. ALL RIGHTS RESERVED.</p>
  <div class="abs follow"><span>FOLLOW US:</span><i></i><i></i><i></i><i></i></div>

</div>
</body>
</html>
```